Letterhead design for business

Looking for an attractive and professional letterhead that uses the logo that is attached below.

Target Market(s)

Potential bankruptcy clients.

Industry/Entity Type

Legal

Colors

Designer to choose colors to be used in the design.

Requirements
Must have
• Address for locations, phone number, and website address.
• Addresses are on website ferncoveadvice.example. Use following phone number (for tracking purposes): 555-013-8274

```html
<!DOCTYPE html>
<html lang="en">
<head>
<meta charset="utf-8">
<title>Ferncove Advice Law Group – Stationery</title>
<link href="https://fonts.googleapis.com/css2?family=Questrial&display=swap" rel="stylesheet">
<style>
  :root {
    --green: #6fb57a;
    --ink: #3a3a3a;
    --rule: #333333;
    --bg: #ececec;
    --paper: #ffffff;
    --panel: #f3f3f3;
    --faint: #e4ece5;
  }
  * { margin: 0; padding: 0; box-sizing: border-box; }
  html, body { width: 1200px; height: 894px; overflow: hidden; }
  body {
    background: var(--bg);
    font-family: "Questrial", "Century Gothic", sans-serif;
    color: var(--ink);
    position: relative;
  }
  .letterhead {
    position: absolute; left: 74px; top: 72px;
    width: 522px; height: 677px;
    background: var(--paper);
  }
  .brand { position: absolute; display: flex; align-items: center; gap: 8px; }
  .brand-dot { border-radius: 50%; background: var(--green); flex: none; }
  .brand-name { color: var(--green); line-height: 1; white-space: nowrap; }
  .brand-sub { color: var(--ink); letter-spacing: 0.18em; line-height: 1; margin-top: 4px; }
  .brand-by { color: var(--green); margin-top: 3px; }
  .brand--header { left: 48px; top: 34px; }
  .brand--header .brand-dot { width: 34px; height: 34px; }
  .brand--header .brand-name { font-size: 21px; }
  .brand--header .brand-sub { font-size: 8px; }
  .brand--header .brand-by { font-size: 7px; }
  .contact {
    position: absolute; right: 42px; top: 35px;
    text-align: right; font-size: 6.4px; line-height: 12px;
  }
  .contact-line { display: flex; justify-content: flex-end; align-items: center; gap: 4px; }
  .contact-icon { width: 8px; height: 8px; border-radius: 50%; background: var(--green); display: inline-flex; align-items: center; justify-content: center; }
  .contact-address { color: var(--green); line-height: 11px; }
  .rule { position: absolute; left: 45px; width: 431px; height: 1px; background: var(--rule); }
  .rule--top { top: 110px; }
  .rule--bottom { top: 645px; }
  .watermark {
    position: absolute; left: 140px; top: 220px; width: 240px; height: 240px;
    border-radius: 50%; background: var(--faint); opacity: 0.6;
  }
  .body-copy {
    position: absolute; left: 55px; top: 140px; width: 411px;
    font-size: 10.6px; line-height: 17.1px; text-align: justify;
  }
  .body-copy p { margin-bottom: 17.1px; }
  .brand--footer { left: 45px; top: 584px; opacity: 0.35; }
  .brand--footer .brand-dot { width: 26px; height: 26px; }
  .brand--footer .brand-name { font-size: 15px; color: #888; }
  .brand--footer .brand-sub { font-size: 6px; color: #888; }
  .signature { position: absolute; left: 379px; top: 572px; }
  .signature-name { font-size: 14px; }
  .signature-title { font-size: 9.5px; margin-top: 8px; }
  .site-url {
    position: absolute; left: 0; width: 100%; top: 654px;
    text-align: center; font-size: 8.5px; letter-spacing: 0.35em; font-weight: bold;
  }
  .back-panel {
    position: absolute; left: 639px; top: 72px;
    width: 498px; height: 677px;
    background: var(--panel); border-radius: 14px; overflow: hidden;
  }
  .back-panel .watermark { left: 200px; top: 270px; width: 330px; height: 330px; }
  .brand--cover { left: 107px; top: 512px; gap: 14px; }
  .brand--cover .brand-dot { width: 70px; height: 70px; }
  .brand--cover .brand-name { font-size: 32px; }
  .brand--cover .brand-sub { font-size: 12px; margin-top: 8px; }
  .brand--cover .brand-by { font-size: 11px; margin-top: 6px; }
</style>
</head>
<body>
  <section class="letterhead">
    <div class="brand brand--header">
      <span class="brand-dot"></span>
      <div>
        <div class="brand-name">Ferncove Advice</div>
        <div class="brand-sub">LAW GROUP</div>
        <div class="brand-by">by Attorney M. Okafor</div>
      </div>
    </div>
    <div class="contact">
      <div class="contact-line">555.013.8274 <span class="contact-icon"></span></div>
      <div class="contact-line">555.014.6630 <span class="contact-icon"></span></div>
      <div class="contact-line">info@ferncoveadvice.example <span class="contact-icon"></span></div>
      <div class="contact-address">1180 Alder Row, Millbrook, Georgia 30999</div>
      <div class="contact-address">45 Harbor Lane, Suite #300 Riverton, Georgia 30998</div>
    </div>
    <div class="rule rule--top"></div>
    <div class="watermark" aria-hidden="true"></div>
    <div class="body-copy">
      <p>Lorem ipsum dolor sit amet, consectetur adipiscing elit. Donec orci purus, luctus vitae dignissim eu, iaculis sed purus. Vivamus faucibus, ipsum nec aliquet viverra, leo mauris condimentum ligula, sit amet sagittis enim ligula quis arcu. Nam egestas tortor id nisi porttitor mattis. In tortor ante, ultricies in suscipit a, tempus non massa. Vivamus et auctor mi. Fusce vel massa nulla. Phasellus nec eros mauris, et scelerisque orci. Donec malesuada orci vitae nulla accumsan porta a id massa.</p>
      <p>Quisque accumsan iaculis magna sit amet fringilla. Maecenas consequat, magna eget tincidunt semper, odio nibh rutrum mi, id feugiat ante nisi eu risus. Vestibulum nunc orci, rhoncus a placerat in, ultricies in mi. Cras mattis varius eros, vel fringilla nisi suscipit eget. Quisque scelerisque sagittis nulla at porttitor. Mauris a justo et tellus interdum tristique. Sed id augue vitae urna euismod commodo aliquet a quam. Pellentesque arcu velit, cursus et malesuada ut, consequat et diam. Nullam erat sem, rhoncus id ullamcorper vitae, rhoncus et arcu. In ultricies ultricies nulla,</p>
      <p>Kut rutrum nisi iaculis at. Donec eu magna a metus ornare faucibus. Fusce aliquet faucibus ultricies. Morbi semper, est id tincidunt gravida, sem arcu adipiscing lacus, ac bibendum nulla leo eu purus. Quisque nec diam sed risus consectetur a ccumsan quis quis nibh. Vestibulum id purus lorem. Donec eu magna a metus ornare faucibus. Fusce aliquet faucibus ultricies. Morbi semper, est id tincidunt gravida, sem arcu adipiscing lacus, ac bibendum nulla leo eu purus. Quisque nec diam sed risus consectetur a ccumsan quis quis nibh. Vestibulum id purus lorem.</p>
    </div>
    <div class="brand brand--footer">
      <span class="brand-dot"></span>
      <div>
        <div class="brand-name">Ferncove Advice</div>
        <div class="brand-sub">LAW GROUP</div>
      </div>
    </div>
    <div class="signature">
      <div class="signature-name">Dana Whitfield</div>
      <div class="signature-title">Co-Founder &amp; CEO</div>
    </div>
    <div class="rule rule--bottom"></div>
    <div class="site-url">www.ferncoveadvice.example</div>
  </section>

  <section class="back-panel">
    <div class="watermark" aria-hidden="true"></div>
    <div class="brand brand--cover">
      <span class="brand-dot"></span>
      <div>
        <div class="brand-name">Ferncove Advice</div>
        <div class="brand-sub">LAW GROUP</div>
        <div class="brand-by">by Attorney M. Okafor</div>
      </div>
    </div>
  </section>
</body>
</html>
```